Verdana Glen Website

I need a design of homepage for a health and wellness center. We considers self to be young and fresh and want something along that design. We want a main picture/logo/design (or all three), and underneath that 4 pictures to depict what services we do. The four services are Orthopedic Rehab, Neurological Rehab, Speech Pathology and Float. I have attached our logo, and some pictures that might be helpful, but the pictures don't have to be included. Here is an example of what I would like it look. http://pixelquarry.com/web-design/contests/brimlotts-website-design-needed-more-work-come-submit-517306/entries/84162975

Health

```html
<!DOCTYPE html>
<html lang="en">
<head>
<meta charset="utf-8">
<title>Verdana Glen</title>
<link href="https://fonts.googleapis.com/css2?family=Bebas+Neue&family=Open+Sans:ital,wght@0,400;0,600;0,700;1,600;1,700&display=swap" rel="stylesheet">
<style>
  :root {
    --green: #a9b155;
    --green-text: #8ea61e;
    --teal: #81b1a5;
    --ink: #4a4a4a;
    --white: #ffffff;
    --footer: #262626;
    --rule: #e6e6e6;
    --hero-a: #b9c6cc;
    --hero-b: #8f9ea8;
    --arrow: #2f7fb5;
  }
  * { margin: 0; padding: 0; box-sizing: border-box; }
  html, body { width: 979px; height: 1200px; overflow: hidden; background: var(--white); }
  body { position: relative; font-family: "Open Sans", Arial, sans-serif; color: var(--ink); }

  /* header */
  .site-header { position: absolute; top: 0; left: 0; width: 979px; height: 49px; background: var(--white); z-index: 5; border-bottom: 1px solid var(--rule); }
  .brand { position: absolute; left: 182px; top: 0; height: 49px; display: flex; align-items: center; gap: 7px; }
  .brand-mark { width: 24px; height: 24px; border-radius: 50%; background: var(--teal); }
  .brand-name { font-size: 21px; font-weight: 400; color: var(--green-text); line-height: 1; letter-spacing: .2px; }
  .main-nav { position: absolute; left: 591px; top: 0; display: flex; height: 49px; border-left: 1px solid var(--rule); }
  .main-nav a { display: flex; align-items: center; padding: 0 11px; font-size: 7.5px; font-weight: 600; color: var(--green-text); text-decoration: none; border-right: 1px solid var(--rule); letter-spacing: .3px; }
  .main-nav a.is-active { box-shadow: inset 0 -4px 0 var(--green); }
  .dropdown { position: absolute; left: 636px; top: 55px; width: 91px; background: var(--white); z-index: 6; box-shadow: 0 1px 3px rgba(0,0,0,.15); }
  .dropdown a { display: block; height: 23px; line-height: 23px; padding-left: 11px; font-size: 7px; color: var(--green-text); text-decoration: none; border-bottom: 1px solid var(--rule); }

  /* hero */
  .hero { position: absolute; top: 49px; left: 0; width: 979px; height: 410px; z-index: 3;
    clip-path: polygon(0 0, 100% 0, 100% 377px, 50% 410px, 0 377px); }
  .hero-photo { position: absolute; inset: 0; background: linear-gradient(135deg, var(--hero-a) 0%, #c9d2d4 45%, var(--hero-b) 100%); }
  .hero-title { position: absolute; top: 200px; width: 100%; text-align: center; font-family: "Bebas Neue", sans-serif; font-weight: 400; font-size: 31px; color: var(--white); letter-spacing: .8px; }
  .hero-subline { position: absolute; top: 230px; width: 100%; text-align: center; font-size: 9px; font-style: italic; font-weight: 700; color: var(--white); }
  .hero-button { position: absolute; left: 437px; top: 250px; width: 103px; height: 23px; background: var(--white); font-size: 7px; font-weight: 700; color: #333; text-align: center; line-height: 23px; letter-spacing: .5px; }
  .hero-arrow { position: absolute; top: 193px; width: 16px; height: 16px; }
  .hero-dots { position: absolute; top: 372px; left: 466px; display: flex; gap: 3px; }
  .hero-dots span { width: 6px; height: 6px; border-radius: 50%; background: var(--white); }
  .hero-dots span.is-current { background: var(--green-text); box-shadow: 0 0 0 1.5px var(--white); }

  /* services */
  .services { position: absolute; top: 420px; left: 0; width: 979px; height: 292px; background: var(--green); z-index: 2;
    clip-path: polygon(0 0, 100% 0, 100% 266px, 50% 292px, 0 266px); }
  .section-title { font-family: "Bebas Neue", sans-serif; font-weight: 400; font-size: 20px; text-align: center; letter-spacing: .5px; }
  .services .section-title { position: absolute; top: 81px; width: 100%; color: var(--white); }
  .service { position: absolute; top: 141px; width: 120px; color: var(--white); }
  .service h3 { font-family: "Bebas Neue", sans-serif; font-weight: 400; font-size: 13px; letter-spacing: .3px; margin-bottom: 2px; }
  .service p { font-size: 7.2px; line-height: 12.3px; }
  .service-divider { position: absolute; top: 142px; width: 1px; height: 160px; background: rgba(255,255,255,.45); }

  /* about */
  .about .section-title { position: absolute; top: 766px; width: 100%; color: var(--green-text); font-size: 21px; }
  .about p { position: absolute; left: 320px; top: 802px; width: 339px; font-size: 7.5px; line-height: 12.3px; text-align: justify; color: #555; }

  /* contact */
  .contact { position: absolute; top: 920px; left: 0; width: 979px; height: 235px; background: var(--teal);
    clip-path: polygon(0 0, 50% 27px, 100% 0, 100% 100%, 0 100%); }
  .contact .section-title { position: absolute; top: 81px; width: 100%; color: var(--white); font-size: 17px; }
  .contact-rule { position: absolute; top: 106px; left: 454px; width: 71px; height: 1px; background: rgba(255,255,255,.7); }
  .contact-item { position: absolute; top: 136px; width: 140px; text-align: center; color: var(--white); font-size: 7.3px; }
  .contact-item svg { display: block; margin: 0 auto 3px; }
  .contact-item em { display: block; font-weight: 700; font-size: 7px; }

  /* footer */
  .site-footer { position: absolute; top: 1155px; left: 0; width: 979px; height: 45px; background: var(--footer); color: #ccc; font-size: 6px; text-align: center; padding-top: 17px; }
</style>
</head>
<body>

<header class="site-header">
  <div class="brand"><span class="brand-mark"></span><span class="brand-name">Verdana Glen</span></div>
  <nav class="main-nav">
    <a href="#">HOME</a>
    <a href="#" class="is-active">SERVICES</a>
    <a href="#">ABOUT</a>
    <a href="#">CONTACT</a>
  </nav>
</header>
<div class="dropdown">
  <a href="#">Orthopedic Rehab</a>
  <a href="#">Neurological Rehab</a>
  <a href="#">Speech Pathology</a>
  <a href="#">Float</a>
</div>

<section class="hero">
  <div class="hero-photo" role="img" aria-label="Bright rehabilitation gym with exercise machines and therapy equipment"></div>
  <h1 class="hero-title">OUR GREAT SLOGAN IS OVER HERE</h1>
  <div class="hero-subline">slogan subline goes right here</div>
  <div class="hero-button">GET IN TOUCH</div>
  <svg class="hero-arrow" style="left:183px" viewBox="0 0 16 16"><circle cx="8" cy="8" r="7" fill="none" stroke="var(--arrow)" stroke-width="1.3"/><path d="M9.5 4.5 6 8l3.5 3.5" fill="none" stroke="var(--arrow)" stroke-width="1.5"/></svg>
  <svg class="hero-arrow" style="left:777px" viewBox="0 0 16 16"><circle cx="8" cy="8" r="7" fill="none" stroke="var(--arrow)" stroke-width="1.3"/><path d="M6.5 4.5 10 8l-3.5 3.5" fill="none" stroke="var(--arrow)" stroke-width="1.5"/></svg>
  <div class="hero-dots"><span class="is-current"></span><span></span><span></span><span></span><span></span></div>
</section>

<section class="services">
  <h2 class="section-title">SERVICES</h2>
  <div class="service" style="left:198px"><h3>ORTHOPEDIC REHAB</h3><p>Lorem ipsum dolor sit amet, consectetur adipisicing elit, sed do eiusmod tempor incididunt ut labore et dolore magna aliqua.</p></div>
  <div class="service-divider" style="left:336px"></div>
  <div class="service" style="left:355px"><h3>NEUROLOGICAL REHAB</h3><p>Lorem ipsum dolor sit amet, consectetur adipisicing elit, sed do eiusmod tempor incididunt ut labore et dolore magna aliqua.</p></div>
  <div class="service-divider" style="left:489px"></div>
  <div class="service" style="left:506px"><h3>SPEECH PATHOLOGY</h3><p>Lorem ipsum dolor sit amet, consectetur adipisicing elit, sed do eiusmod tempor incididunt ut labore et dolore magna aliqua.</p></div>
  <div class="service-divider" style="left:642px"></div>
  <div class="service" style="left:662px"><h3>FLOAT</h3><p>Lorem ipsum dolor sit amet, consectetur adipisicing elit, sed do eiusmod tempor incididunt ut labore et dolore magna aliqua.</p></div>
</section>

<section class="about">
  <h2 class="section-title">ABOUT</h2>
  <p>Lorem ipsum dolor sit amet, consectetur adipisicing elit, sed do eiusmod tempor incididunt ut labore et dolore magna aliqua. Ut enim ad minim veniam, quis nostrud exercitation ullamco laboris nisi ut aliquip ex ea commodo consequat. Duis aute irure dolor in reprehenderit in voluptate velit esse cillum dolore eu fugiat nulla pariatur. Excepteur sint occaecat cupidatat non proident, sunt in culpa qui officia deserunt mollit anim id est laborum.</p>
</section>

<section class="contact">
  <h2 class="section-title">CONTACT US</h2>
  <div class="contact-rule"></div>
  <div class="contact-item" style="left:283px">
    <svg width="22" height="28" viewBox="0 0 22 28"><rect x="1" y="1" width="20" height="26" rx="2" fill="none" stroke="#fff" stroke-width="1.6"/><circle cx="11" cy="22" r="1.4" fill="#fff"/></svg>
    +1 (555) 014 2276
  </div>
  <div class="contact-item" style="left:419px">
    <svg width="34" height="28" viewBox="0 0 34 28"><rect x="1" y="1" width="32" height="26" fill="none" stroke="#fff" stroke-width="1.6"/><path d="M1 1l16 14L33 1M1 27l12-12M33 27 21 15" fill="none" stroke="#fff" stroke-width="1.6"/></svg>
    info@verdanaglen.com<em>click to write us</em>
  </div>
  <div class="contact-item" style="left:558px">
    <svg width="22" height="28" viewBox="0 0 22 28"><path d="M11 27C11 27 2 16 2 10a9 9 0 0 1 18 0c0 6-9 17-9 17z" fill="none" stroke="#fff" stroke-width="1.6"/><circle cx="11" cy="10" r="3.5" fill="none" stroke="#fff" stroke-width="1.6"/></svg>
    18 Fernbrook Ave, NY, NY<em>click to find us on maps</em>
  </div>
</section>

<footer class="site-footer">©2014 Verdana Glen. All Rights Reserved</footer>

</body>
</html>
```